Author/ Speaker Business Card design

I need a business card designed that will go with the branding that is already on my book and website. I like clean and straightforward, but I am not opposed to something more 'innovative'.

Target Market(s)

Colleges and Universities, educational institutions

Industry/Entity Type

Education

Contact Information for Business Card

Standard size. It should be able to be printed on good quality white or ivory paper.

Font styles to use
Sans Serif

Colors
0355a3

Requirements
Must have
• There's a blue on my website. It should have some blue. My logo is at the top. It should have the logo incorporated somewhere on it. My name, Author | Speaker | Teacher | Trainer, my phone number (+31 64-207 5819), my email address (milo@theboldlearner.example), Social media icons (twitter, Instagram, LinkedIn) with the addresses (twitter @writermilofenwick, Instagram - theboldlearner, LinkedIn - theboldlearner) By they way, the website is www.theboldlearner.example. There is a photo of the book on the website. Also, my full name is Milo Fenwick
Nice to have
• Try to use the font that is on the website and book. Also, if you could get that blue, that would be great.
Should not have
• My photo

```html
<!DOCTYPE html>
<html lang="en">
<head>
<meta charset="utf-8">
<title>The Bold Learner – Business Card</title>
<link rel="stylesheet" href="https://fonts.googleapis.com/css2?family=Open+Sans:wght@400;600;700&display=swap">
<style>
  :root {
    --brand-blue: #0355a3;
    --brand-blue-deep: #06378a;
    --ink-grey: #8a8d92;
    --rule-grey: #a9abae;
    --paper: #f6f6f6;
    --paper-edge: #e9e9e9;
    --stage: #1d1e20;
    --white: #ffffff;
  }
  * { box-sizing: border-box; margin: 0; padding: 0; }
  html, body { width: 1200px; height: 900px; overflow: hidden; }
  body {
    background: var(--stage);
    font-family: "Open Sans", Arial, sans-serif;
    position: relative;
  }
  .card {
    position: absolute;
    left: 320px;
    width: 560px;
    height: 320px;
    border-radius: 3px;
    overflow: hidden;
  }
  /* Front */
  .card-front {
    top: 80px;
    background: linear-gradient(160deg, var(--white), var(--paper) 55%, var(--paper-edge));
  }
  .front-wordmark {
    position: absolute;
    left: 150px;
    top: 42px;
    display: flex;
    align-items: center;
    gap: 14px;
    color: var(--brand-blue);
    font-weight: 700;
    font-size: 34px;
    letter-spacing: -0.5px;
  }
  .wordmark-dot {
    width: 22px; height: 22px;
    border-radius: 50%;
    background: var(--brand-blue);
  }
  .person {
    position: absolute;
    left: 34px;
    top: 130px;
  }
  .person-name {
    color: var(--brand-blue);
    font-weight: 700;
    font-size: 19px;
    line-height: 1.1;
  }
  .person-title {
    color: var(--ink-grey);
    font-size: 12px;
    margin-top: 2px;
  }
  .person-rule {
    position: absolute;
    left: 0; top: 176px;
    width: 190px; height: 2px;
    background: var(--brand-blue);
  }
  .card-rule {
    position: absolute;
    left: 0; right: 0; top: 178px;
    height: 1px;
    background: var(--rule-grey);
  }
  .contact-list {
    position: absolute;
    left: 34px;
    top: 190px;
    list-style: none;
    font-size: 12.5px;
    color: var(--ink-grey);
    line-height: 21px;
  }
  .contact-list li { display: flex; align-items: center; gap: 8px; }
  .contact-list svg { width: 12px; height: 12px; fill: none; stroke: var(--brand-blue); stroke-width: 1.6; }
  .contact-web { color: var(--brand-blue); }
  .roles {
    position: absolute;
    right: 34px;
    bottom: 26px;
    font-size: 13px;
    color: var(--ink-grey);
    letter-spacing: 0.3px;
  }
  .roles .sep { color: var(--brand-blue); padding: 0 4px; }

  /* Back */
  .card-back {
    top: 500px;
    background: linear-gradient(135deg, #0d63b4, var(--brand-blue) 45%, var(--brand-blue-deep));
    color: var(--white);
  }
  .back-wordmark {
    position: absolute;
    left: 0; right: 0; top: 96px;
    display: flex;
    justify-content: center;
    align-items: center;
    gap: 16px;
    font-weight: 700;
    font-size: 44px;
    letter-spacing: -0.5px;
  }
  .back-wordmark .wordmark-dot { background: var(--white); width: 28px; height: 28px; }
  .social-list {
    position: absolute;
    left: 0; right: 0; bottom: 48px;
    display: flex;
    justify-content: center;
    gap: 22px;
    list-style: none;
    font-size: 12.5px;
  }
  .social-list li { display: flex; align-items: center; gap: 7px; }
  .social-dot {
    width: 11px; height: 11px;
    border-radius: 50%;
    background: var(--white);
  }
</style>
</head>
<body>

<section class="card card-front" aria-label="Business card front">
  <div class="front-wordmark"><span class="wordmark-dot"></span>The Bold Learner</div>

  <div class="person">
    <p class="person-name">Milo Fenwick</p>
    <p class="person-title">Managing Director</p>
  </div>
  <div class="card-rule"></div>
  <div class="person-rule"></div>

  <ul class="contact-list">
    <li>
      <svg viewBox="0 0 12 12"><path d="M2.5 1.5l2 2-1 1.3c.6 1.4 1.6 2.4 3 3l1.3-1 2 2-1.3 1.5C5 10 2 7 1 2.8z"/></svg>
      +31 64-207 5819
    </li>
    <li>
      <svg viewBox="0 0 12 12"><rect x="1" y="2.5" width="10" height="7"/><path d="M1 2.5l5 4 5-4"/></svg>
      milo@theboldlearner.example
    </li>
    <li class="contact-web">
      <svg viewBox="0 0 12 12"><circle cx="6" cy="6" r="5"/><ellipse cx="6" cy="6" rx="2.2" ry="5"/><path d="M1 6h10"/></svg>
      www.theboldlearner.example
    </li>
  </ul>

  <p class="roles">Author<span class="sep">/</span>Speaker<span class="sep">/</span>Teacher<span class="sep">/</span>Trainer</p>
</section>

<section class="card card-back" aria-label="Business card back">
  <div class="back-wordmark"><span class="wordmark-dot"></span>The Bold Learner</div>
  <ul class="social-list">
    <li><span class="social-dot"></span>@writermilofenwick</li>
    <li><span class="social-dot"></span>/theboldlearner</li>
    <li><span class="social-dot"></span>/theboldlearner</li>
  </ul>
</section>

</body>
</html>
```